Basic Company webpage with the elements and colors of our Logo

Basic Home page with a few pages:
- Home,
- About US,
- Contact us
- Services

Target Market(s)

Business Customers (B2B)

Coding

Coded - Design and coding required

Number of Pages Required

5+ page

Requirements
Must have
• Professional, Clean, Simple High Tech, Contact should have a contact us dialog for sending messages to us
Nice to have
• Meet with us links for calendar access though MS Bookings

```html
<!DOCTYPE html>
<html lang="en">
<head>
<meta charset="utf-8">
<title>Northbeam IT Group</title>
<link href="https://fonts.googleapis.com/css2?family=Open+Sans:wght@400;600;700&family=Montserrat:wght@400;500;600&family=Arimo:wght@400&family=Tinos&display=swap" rel="stylesheet">
<style>
:root{
  --navy:#0b4466;
  --deep:#0f2356;
  --ink:#0d1327;
  --orange:#fbae3c;
  --text:#6b7280;
  --light:#f0f0f0;
  --pale:#f5f7fb;
}
*{margin:0;padding:0;box-sizing:border-box}
html,body{width:1200px;height:4298px;overflow:hidden}
body{position:relative;font-family:"Open Sans",sans-serif;background:#fff;color:#333}
.abs{position:absolute}
.header{left:0;top:0;width:1200px;height:145px;background:#f4f8fd}
.brand{left:70px;top:38px;font:700 30px "Open Sans",sans-serif;color:var(--navy);display:flex;align-items:center;gap:12px}
.brand i{width:22px;height:22px;border-radius:50%;background:var(--orange);display:block}
.contact-item{top:34px;display:flex;gap:12px;align-items:center;font:400 13px Arimo,sans-serif;color:#444;line-height:20px}
.contact-item .ico{width:34px;height:34px;border:2px solid #3bbfa6;transform:rotate(45deg);border-radius:4px;display:flex;align-items:center;justify-content:center}
.contact-item .ico svg{transform:rotate(-45deg)}
.nav{left:243px;top:110px;width:884px;height:53px;background:#fff;border-radius:27px;box-shadow:0 2px 6px rgba(0,0,0,.12)}
.nav a{position:absolute;top:17px;font:400 14px Arimo,sans-serif;color:#333;text-decoration:none}
.btn-appt{left:968px;top:113px;width:156px;height:45px;background:var(--orange);border-radius:23px;color:#fff;font:400 14px Arimo,sans-serif;text-align:center;line-height:45px;box-shadow:2px 2px 0 #fff,3px 3px 4px rgba(0,0,0,.2)}
.hero{left:0;top:145px;width:1200px;height:900px;background:linear-gradient(100deg,#14306e 0%,#2a4a82 45%,#6d7f9c 75%,#9aa5b5 100%)}
.hero-box{left:90px;top:345px;width:535px;height:300px;background:rgba(30,50,90,.55)}
.hero-box .bar{position:absolute;left:0;top:40px;width:4px;height:82px;background:var(--orange)}
.hero-box h1{position:absolute;left:28px;top:30px;font:600 38px/49px "Open Sans",sans-serif;color:#fff}
.hero-box p{position:absolute;left:30px;top:145px;width:490px;font:400 15px/30px "Open Sans",sans-serif;color:#fff}
.btn-demo{left:118px;top:567px;width:198px;height:45px;background:var(--orange);color:#fff;font:600 14px/45px "Open Sans",sans-serif;text-align:center}
.eyebrow{font:400 12px Montserrat,sans-serif;color:var(--orange);padding-bottom:5px;border-bottom:1px solid var(--orange)}
.about-photo{left:0;top:1015px;width:455px;height:417px;border-radius:0 230px 0 0;background:linear-gradient(135deg,#8a7a6a,#c9b6a0 50%,#5a6a78);border-right:8px solid var(--navy)}
.about-dot{left:362px;top:1052px;width:120px;height:120px;border-radius:50%;background:#e6eef6}
.h2{font:700 36px/46px "Open Sans",sans-serif;color:var(--navy)}
.body-text{font:400 12px/19px "Open Sans",sans-serif;color:var(--text)}
.btn-contact{left:604px;top:1315px;width:136px;height:40px;background:var(--orange);color:#fff;font:600 14px/40px "Open Sans",sans-serif;padding-left:14px}
.services{left:0;top:1432px;width:1200px;height:663px;background:var(--light)}
.svc-photo{top:1653px;width:305px;height:282px;background:linear-gradient(160deg,#cfd3d6,#7d858c)}
.svc-card{top:1880px;width:238px;height:142px;background:#fff;box-shadow:0 3px 8px rgba(0,0,0,.08)}
.svc-card h3{position:absolute;left:22px;top:30px;font:600 15px "Open Sans",sans-serif;color:var(--navy)}
.svc-card p{position:absolute;left:20px;top:64px;width:210px;font:400 12px/20px "Open Sans",sans-serif;color:var(--text)}
.svc-ico{top:1852px;width:60px;height:60px;border-radius:50%;background:var(--orange);border:3px solid #fff;display:flex;align-items:center;justify-content:center}
.why{left:0;top:2095px;width:1200px;height:575px;background:linear-gradient(90deg,#b89a7a 0%,#8a8c90 35%,#1a3068 60%,#0f2356 100%)}
.why-item{left:625px;width:442px;height:105px;background:rgba(40,60,130,.75);border-left:4px solid #cfd6e4}
.why-item.active{border-left-color:var(--orange)}
.why-item h4{position:absolute;left:92px;top:25px;font:600 14px "Open Sans",sans-serif;color:#fff}
.why-item p{position:absolute;left:92px;top:46px;width:320px;font:400 12.5px/20px "Open Sans",sans-serif;color:#e8ecf5}
.why-item svg{position:absolute;left:28px;top:32px}
.testi{left:0;top:2670px;width:1200px;height:610px;background:var(--pale)}
.quote{top:2898px;width:305px;height:174px;background:#fff;box-shadow:0 2px 8px rgba(0,0,0,.06);padding:26px 22px;font:400 15px/23px Montserrat,sans-serif;color:#444}
.quote.featured{background:var(--navy);color:#fff}
.quote:after{content:"";position:absolute;left:0;bottom:-20px;border-top:20px solid var(--orange);border-right:20px solid transparent}
.person{top:3100px;display:flex;gap:20px;align-items:center}
.person .av{width:55px;height:55px;border-radius:50%;background:linear-gradient(#aab4c0,#5b6878);border:3px solid #fff;box-shadow:0 1px 4px rgba(0,0,0,.2)}
.person b{display:block;font:600 14px Montserrat,sans-serif;color:#222}
.person span{font:400 12px Montserrat,sans-serif;color:#999}
.dot{top:3199px;height:9px;border-radius:5px;background:#1677d2}
.touch{left:0;top:3325px;width:1200px;text-align:center;font:400 46px Tinos,serif;color:var(--navy)}
.touch em{font-style:normal;color:var(--orange)}
.form-box{left:147px;top:3430px;width:908px;height:290px;background:#fff;box-shadow:0 2px 10px rgba(0,0,0,.08)}
.addr{left:0;top:0;width:303px;height:290px;background:var(--light)}
.addr h3{position:absolute;left:33px;top:32px;font:400 36px Tinos,serif;color:#333}
.addr .line{position:absolute;left:33px;display:flex;gap:10px;font:400 13px/19px "Open Sans",sans-serif;color:#222}
.field{position:absolute;font:400 13px "Open Sans",sans-serif;color:#333;border-bottom:1px solid #999;height:26px}
.btn-enq{left:325px;top:213px;width:186px;height:37px;border-radius:19px;background:var(--orange);color:#fff;font:400 13px/37px Tinos,serif;text-align:center}
.footer{left:0;top:3930px;width:1200px;height:368px;background:var(--ink)}
.f-bar{top:4060px;width:272px;height:60px;border-top:6px solid #1b2338;border-bottom:6px solid #1b2338;display:flex;align-items:center;justify-content:center;gap:10px;color:#fff}
.f-nav a{position:absolute;top:4217px;font:400 13px "Open Sans",sans-serif;color:#fff;text-decoration:none}
.social{top:4157px;width:18px;height:18px;border-radius:50%;background:#fff}
</style>
</head>
<body>

<div class="abs header"></div>
<div class="abs brand"><i></i>Northbeam IT Group</div>

<div class="abs contact-item" style="left:415px"><div class="ico"><svg width="14" height="14" viewBox="0 0 24 24"><path d="M12 2a7 7 0 0 0-7 7c0 5 7 13 7 13s7-8 7-13a7 7 0 0 0-7-7zm0 9.5A2.5 2.5 0 1 1 12 6.5a2.5 2.5 0 0 1 0 5z" fill="#3bbfa6"/></svg></div><div>Email Address<br>contact@northbeam-it.example</div></div>
<div class="abs contact-item" style="left:662px"><div class="ico"><svg width="14" height="14" viewBox="0 0 24 24"><path d="M12 2a7 7 0 0 0-7 7c0 5 7 13 7 13s7-8 7-13a7 7 0 0 0-7-7zm0 9.5A2.5 2.5 0 1 1 12 6.5a2.5 2.5 0 0 1 0 5z" fill="#3bbfa6"/></svg></div><div>Email Address<br>contact@northbeam-it.example</div></div>
<div class="abs contact-item" style="left:908px"><div class="ico"><svg width="14" height="14" viewBox="0 0 24 24"><path d="M12 2a7 7 0 0 0-7 7c0 5 7 13 7 13s7-8 7-13a7 7 0 0 0-7-7zm0 9.5A2.5 2.5 0 1 1 12 6.5a2.5 2.5 0 0 1 0 5z" fill="#3bbfa6"/></svg></div><div>Email Address<br>contact@northbeam-it.example</div></div>

<div class="abs hero" role="img" aria-label="Photo of business people meeting at a table in a modern office, blue tint"></div>

<nav class="abs nav">
  <a style="left:68px">Home</a>
  <a style="left:158px">About Us</a>
  <a style="left:245px">Services</a>
  <a style="left:328px">Our Team</a>
  <a style="left:427px">Projects</a>
</nav>
<div class="abs btn-appt">Appointment</div>

<svg class="abs" style="left:0;top:760px" width="1200" height="290" viewBox="0 760 1200 290">
  <path d="M0 830 C 350 790 800 760 1200 1000 L1200 1050 L0 1050 Z" fill="#fff"/>
  <path d="M470 812 C 800 800 1050 900 1200 995 L1200 1045 C 1050 920 800 830 470 812 Z" fill="#fbae3c"/>
</svg>

<div class="abs hero-box">
  <div class="bar"></div>
  <h1>Securing Your Digital<br>Future</h1>
  <p>It is a long and established fact that a reader will be distracted by the readable content of a page when looking.</p>
</div>
<div class="abs btn-demo">REQUEST A DEMO</div>

<div class="abs about-photo" role="img" aria-label="Photo of two smiling businessmen looking at a tablet"></div>
<div class="abs about-dot"></div>
<div class="abs eyebrow" style="left:604px;top:993px">WHO WE ARE</div>
<h2 class="abs h2" style="left:604px;top:1026px">Your Partner in IT<br>Excellence</h2>
<div class="abs" style="left:604px;top:1145px;font:400 18px 'Open Sans',sans-serif;color:var(--navy)">Your Gateway to Innovative IT Solutions</div>
<p class="abs body-text" style="left:604px;top:1182px;width:460px">Lorem ipsum dolor sit amet, consectetur adipiscing elit, sed do eiusmod temp or incididunt ut labore et dolore magna aliqua. Ut enim ad minim veniam, quis laboris nisi ut aliquip ex ea commodo consequat.</p>
<p class="abs body-text" style="left:604px;top:1251px;width:460px">Lorem ipsum dolor sit amet, consectetur adipiscing elit, sed do eiusmod temp or incididunt ut labore et dolore magna aliqua.</p>
<div class="abs btn-contact">Contact us <svg width="18" height="10" viewBox="0 0 18 10" style="margin-left:10px"><path d="M0 5h16M12 1l4 4-4 4" stroke="#fff" stroke-width="1.5" fill="none"/></svg></div>

<div class="abs services"></div>
<div class="abs eyebrow" style="left:557px;top:1522px">OUR SERVICES</div>
<h2 class="abs h2" style="left:0;width:1200px;text-align:center;top:1560px;font-size:40px">Services We Provide</h2>

<div class="abs svc-photo" style="left:118px" role="img" aria-label="Photo of colleagues discussing at a desk"></div>
<div class="abs svc-photo" style="left:447px" role="img" aria-label="Photo of a woman holding a tablet in an office"></div>
<div class="abs svc-photo" style="left:774px" role="img" aria-label="Photo of colleagues reviewing a laptop together"></div>
<div class="abs svc-card" style="left:185px"><h3>IT Procurement</h3><p>Lorem ipsum dolor sit amet, co nsectetur adipiscing elit, s</p></div>
<div class="abs svc-card" style="left:514px"><h3>Data Management</h3><p>Lorem ipsum dolor sit amet, co nsectetur adipiscing elit, s</p></div>
<div class="abs svc-card" style="left:841px"><h3>Security Solutions</h3><p>Lorem ipsum dolor sit amet, co nsectetur adipiscing elit, s</p></div>
<div class="abs svc-ico" style="left:155px"><svg width="28" height="28" viewBox="0 0 24 24" fill="none" stroke="#fff" stroke-width="1.5"><circle cx="10" cy="7" r="4"/><path d="M3 21c1-5 4-7 7-7m3 7l6-6 2 2-6 6h-2z"/></svg></div>
<div class="abs svc-ico" style="left:484px"><svg width="28" height="28" viewBox="0 0 24 24" fill="none" stroke="#fff" stroke-width="1.5"><circle cx="10" cy="7" r="4"/><path d="M3 21c1-5 4-7 7-7m3 7l6-6 2 2-6 6h-2z"/></svg></div>
<div class="abs svc-ico" style="left:811px"><svg width="28" height="28" viewBox="0 0 24 24" fill="none" stroke="#fff" stroke-width="1.5"><circle cx="10" cy="7" r="4"/><path d="M3 21c1-5 4-7 7-7m3 7l6-6 2 2-6 6h-2z"/></svg></div>

<div class="abs why" role="img" aria-label="Photo of a team of professionals talking in a bright office, fading into navy"></div>
<div class="abs eyebrow" style="left:620px;top:2143px">WHY CHOOSE US</div>
<h2 class="abs h2" style="left:620px;top:2175px;color:#fff">Shielding Your Data<br>from Cyber Crime</h2>
<div class="abs why-item active" style="top:2285px"><svg width="36" height="36" viewBox="0 0 24 24" fill="none" stroke="#fff" stroke-width="1.3"><circle cx="10" cy="7" r="4"/><path d="M3 21c1-5 4-7 7-7m3 7l6-6 2 2-6 6h-2z"/></svg><h4>CLIENT-CENTRIC</h4><p>Lorem ipsum dolor sit amet, consectetur adipiscing elit, sed do eiusmod tempor incidid</p></div>
<div class="abs why-item" style="top:2398px"><svg width="36" height="36" viewBox="0 0 24 24" fill="none" stroke="#fff" stroke-width="1.3"><path d="M12 2l9 7-3 11H6L3 9z"/><circle cx="12" cy="12" r="3"/></svg><h4>PROFESSIONALISM</h4><p>Lorem ipsum dolor sit amet, consectetur adipiscing elit, sed do eiusmod tempor incidid</p></div>
<div class="abs why-item" style="top:2510px"><svg width="36" height="36" viewBox="0 0 24 24" fill="none" stroke="#fff" stroke-width="1.3"><path d="M4 19a9 9 0 1 1 16 0"/><path d="M12 14l3-5"/><circle cx="12" cy="15" r="1.5"/></svg><h4>EXPERIENCED EXPERTS</h4><p>Lorem ipsum dolor sit amet, consectetur adipiscing elit, sed do eiusmod tempor incidid</p></div>

<div class="abs testi"></div>
<div class="abs eyebrow" style="left:555px;top:2764px">TESTIMONIALS</div>
<h2 class="abs h2" style="left:0;width:1200px;text-align:center;top:2802px;font-size:40px">What Clients are Saying</h2>
<div class="abs quote" style="left:118px">Lorem ipsum dolor sit amet, consectetur adipiscing elit, sed d o eiusmod tempor incididunt ut lab ore et dolore magna aliqua. Ut enim ad min</div>
<div class="abs quote featured" style="left:447px">Lorem ipsum dolor sit amet, consectetur adipiscing elit, sed d o eiusmod tempor incididunt ut lab ore et dolore magna aliqua. Ut enim ad min</div>
<div class="abs quote" style="left:776px">Lorem ipsum dolor sit amet, consectetur adipiscing elit, sed d o eiusmod tempor incididunt ut lab ore et dolore magna aliqua. Ut enim ad min</div>
<div class="abs person" style="left:136px"><div class="av" role="img" aria-label="Client portrait"></div><div><b>Jhon Smith</b><span>Engineer</span></div></div>
<div class="abs person" style="left:464px"><div class="av" role="img" aria-label="Client portrait"></div><div><b>Jhon Smith</b><span>Engineer</span></div></div>
<div class="abs person" style="left:794px"><div class="av" role="img" aria-label="Client portrait"></div><div><b>Jhon Smith</b><span>Engineer</span></div></div>
<div class="abs dot" style="left:570px;width:22px"></div>
<div class="abs dot" style="left:596px;width:9px"></div>
<div class="abs dot" style="left:609px;width:9px"></div>
<div class="abs dot" style="left:622px;width:9px"></div>

<h2 class="abs touch">Get In <em>Touch</em></h2>
<div class="abs form-box">
  <div class="abs addr">
    <h3>Address</h3>
    <div class="line" style="top:100px"><svg width="20" height="20" viewBox="0 0 24 24" fill="none" stroke="#fbae3c" stroke-width="1.5"><circle cx="10" cy="7" r="4"/><path d="M3 21c1-5 4-7 7-7m3 7l6-6 2 2-6 6h-2z"/></svg><span>Company Name<br>Place 2134 Ave<br>City, Country</span></div>
    <div class="line" style="top:175px;font-weight:600"><svg width="20" height="20" viewBox="0 0 24 24" fill="none" stroke="#fbae3c" stroke-width="1.5"><path d="M5 3h4l2 5-3 2a12 12 0 0 0 6 6l2-3 5 2v4a2 2 0 0 1-2 2A17 17 0 0 1 3 5a2 2 0 0 1 2-2z"/></svg><span>555-010-2040 Or 555-010-3090</span></div>
    <div class="line" style="top:215px"><svg width="20" height="20" viewBox="0 0 24 24" fill="none" stroke="#fbae3c" stroke-width="1.5"><rect x="4" y="3" width="16" height="18" rx="2"/><circle cx="12" cy="10" r="3"/><path d="M7 18c1-3 9-3 10 0"/></svg><span>info@northbeam-it.example</span></div>
  </div>
  <div class="field" style="left:325px;top:45px;width:265px">Name:</div>
  <div class="field" style="left:625px;top:45px;width:265px"></div>
  <div class="field" style="left:325px;top:91px;width:265px">Phone:</div>
  <div class="field" style="left:625px;top:91px;width:265px"></div>
  <div class="field" style="left:325px;top:134px;width:565px;height:50px">Details:</div>
  <div class="abs btn-enq">QUICK ENQUIRY &nbsp;→</div>
</div>

<svg class="abs" style="left:0;top:3660px" width="1200" height="280" viewBox="0 3660 1200 280">
  <path d="M0 3680 C 120 3830 420 3920 720 3930 L1200 3930 L1200 3940 L0 3940 Z" fill="#0d1327"/>
  <path d="M0 3660 C 150 3820 420 3905 720 3925 C 420 3915 140 3850 0 3740 Z" fill="#fbae3c"/>
</svg>
<div class="abs footer"></div>
<div class="abs f-bar" style="left:175px;font:400 12px/15px 'Open Sans',sans-serif"><svg width="14" height="18" viewBox="0 0 24 24"><path d="M12 2a7 7 0 0 0-7 7c0 5 7 13 7 13s7-8 7-13a7 7 0 0 0-7-7zm0 9.5A2.5 2.5 0 1 1 12 6.5a2.5 2.5 0 0 1 0 5z" fill="#1677d2"/></svg><span>107 N 123 STREET<br>COUNTRY</span></div>
<div class="abs" style="left:470px;top:4062px;width:260px;text-align:center;font:700 24px 'Open Sans',sans-serif;color:var(--navy)">Northbeam IT Group</div>
<div class="abs f-bar" style="left:760px;font:400 21px 'Open Sans',sans-serif"><svg width="14" height="18" viewBox="0 0 24 24"><path d="M12 2a7 7 0 0 0-7 7c0 5 7 13 7 13s7-8 7-13a7 7 0 0 0-7-7zm0 9.5A2.5 2.5 0 1 1 12 6.5a2.5 2.5 0 0 1 0 5z" fill="#1677d2"/></svg><span>555 010 4477</span></div>
<div class="abs" style="left:0;width:1200px;text-align:center;top:4128px;font:400 12px 'Open Sans',sans-serif;color:#1677d2">info@northbeam-it.example</div>
<div class="abs social" style="left:539px"></div>
<div class="abs social" style="left:566px"></div>
<div class="abs social" style="left:593px"></div>
<div class="abs social" style="left:620px"></div>
<div class="abs social" style="left:647px"></div>
<div class="f-nav">
  <a style="left:278px">HOME</a>
  <a style="left:352px">SERVICES</a>
  <a style="left:452px">ABOUT US</a>
  <a style="left:558px">PROJECTS</a>
  <a style="left:658px">TESTIMONIALS</a>
  <a style="left:796px">FAQ</a>
  <a style="left:864px">CONTACT US</a>
</div>

</body>
</html>
```